Visitenkarten-Design für German Consulting Company
Zielgruppe
We are a German Consulting Company, who specialized in public sector Software development (www.qrt-beratung.de).
Our customers are audit offices all over Germany. We offer 3 custom software solution’s to our customers. Those three software solutions form a Software-Suite.
Our three products are called: qrt clearScope, qrt ledgerPilot and qrt ledgerWriter..
You can find the 3 Logos for our products enclosed
Wir sind eine Unternehmensberatung, die sich auf Softwareentwicklung für den Public Sektor spezialisiert hat (www.qrt-beratung.de). Unsere Zielgruppe sind Rechnungsprüfungsämter in ganz Deutschland. Wir bieten für diesen Markt drei abgestimmte Softwareprodukte an, die zusammen eine Software-Suite bilden. Die drei Produkte sind der qrt clearScope, der qrt ledgerWriter und der qrt ledgerPilot.
Aufgabenstellung
For activation, our software needs a licence key. This Key is sent to our customers with a nice box an the requird documentation.
The licence Key is supposed to be printed onto a metal card.
We are looking for a design regarding those „licencecards“
You can find the avaliable options for materials and customizations here: https://www.karten-stahl-vp.example/optionen/
The card has at least to show the following Information’s:
Company Logo and
licencekey: 8416 9072 5831 6049
We are going for a clean, professional and high value look.
Unsere Produkte benötigen einen Lizenzschlüssel um aktiviert zu werden. Dieser Lizenzschlüssel wird mit den dazugehörigen Handbüchern in einer edlen Verpackung übergeben. Der Lizenzschlüssel soll auf einer Metallkarte aufgebracht werden, wie Sie diese Firma anbietet: https://www.karten-stahl-vp.example/.
Materialien und Verabreitungsmöglichkeiten werden hier aufgeführt: https://www.karten-stahl-vp.example/optionen/
Die Karte muss mindestens unser Firmenlogo und eine 16 Stellige Lizenznummer(8416 9072 5831 604) enthalten.
Die Karte soll clean, professionell und hochwertig aussehen und wenige Farben verwenden .

```html
<!DOCTYPE html>
<html lang="de">
<head>
<meta charset="utf-8">
<title>Lizenzkarte – qrt</title>
<link href="https://fonts.googleapis.com/css2?family=Montserrat:wght@400;500;700&display=swap" rel="stylesheet">
<style>
  :root {
    --bg: #d9d9d9;
    --card: #ffffff;
    --ink: #1f2124;
    --accent: #e3141b;
    --shadow: rgba(0, 0, 0, 0.18);
  }
  * { box-sizing: border-box; margin: 0; padding: 0; }
  html, body { width: 1200px; height: 750px; overflow: hidden; }
  body {
    background: var(--bg);
    font-family: "Montserrat", Arial, sans-serif;
    color: var(--ink);
    position: relative;
  }
  .card {
    position: absolute;
    top: 230px;
    width: 500px;
    height: 290px;
    background: var(--card);
    border-radius: 28px;
    box-shadow: 0 8px 24px var(--shadow);
    overflow: hidden;
  }
  .card--contact { left: 60px; }
  .card--licence { left: 640px; }

  /* contact side */
  .person { position: absolute; left: 34px; top: 36px; }
  .person__name { font-size: 15px; font-weight: 700; }
  .person__role { font-weight: 400; }
  .person__lines { display: flex; gap: 16px; margin-top: 5px; font-size: 11.5px; }
  .icon-line { display: flex; align-items: center; gap: 5px; }
  .icon-line svg { width: 12px; height: 12px; flex: none; }

  .company { position: absolute; left: 34px; top: 130px; font-size: 11.5px; line-height: 1.35; }
  .company__name { font-weight: 700; }
  .central { position: absolute; left: 34px; top: 182px; font-size: 11.5px; line-height: 1.35; }
  .central__label { font-weight: 700; }
  .web { position: absolute; left: 34px; bottom: 30px; font-size: 12px; font-weight: 700; }

  /* licence side */
  .licence { position: absolute; left: 34px; top: 40px; }
  .licence__label { font-size: 17px; font-weight: 700; letter-spacing: 0.04em; }
  .licence__key { font-size: 14px; font-weight: 400; letter-spacing: 0.04em; margin-top: 3px; }
  .rule { position: absolute; height: 1px; background: var(--accent); right: 0; }
  .rule--top { left: 230px; top: 52px; }
  .rule--bottom { left: 290px; top: 244px; }

  .brand { position: absolute; left: 34px; bottom: 36px; display: flex; align-items: center; gap: 8px; }
  .brand__mark { width: 12px; height: 12px; background: var(--accent); }
  .brand__name { font-size: 15px; font-weight: 700; color: var(--ink); }
</style>
</head>
<body>

  <section class="card card--contact" aria-label="Kontaktseite">
    <div class="person">
      <p class="person__name">Dr. Martin Korbel <span class="person__role">/ Geschäftsführer</span></p>
      <div class="person__lines">
        <span class="icon-line">
          <svg viewBox="0 0 12 12" aria-hidden="true"><path d="M2.5 1 L4.5 1 L5.3 3.2 L4 4.3 Q5 6.8 7.7 8 L8.8 6.7 L11 7.5 L11 9.5 Q11 11 9.5 11 Q1 10 1 2.5 Q1 1 2.5 1 Z" fill="var(--accent)"/></svg>
          0049 6221 47310 214
        </span>
        <span class="icon-line">
          <svg viewBox="0 0 12 12" aria-hidden="true"><rect x="0.5" y="2.5" width="11" height="7" fill="var(--accent)"/><path d="M0.5 2.5 L6 7 L11.5 2.5" stroke="#fff" stroke-width="1" fill="none"/></svg>
          m.korbel@qrt-beratung.de
        </span>
      </div>
    </div>

    <div class="company">
      <p class="company__name">qrt Beratungssysteme GmbH <span class="person__role">· Technologiepark</span></p>
      <p>Lindenweg 14 · 69115 Heidelberg</p>
    </div>

    <div class="central">
      <p class="central__label">Zentrale:</p>
      <p>0049 6221 47310 0</p>
      <p>info@qrt-beratung.de</p>
    </div>

    <p class="web icon-line">
      <svg viewBox="0 0 12 12" aria-hidden="true"><circle cx="6" cy="6" r="5.5" fill="var(--accent)"/><path d="M0.5 6 H11.5 M6 0.5 V11.5 M1.5 3.3 H10.5 M1.5 8.7 H10.5" stroke="#fff" stroke-width="0.7"/><ellipse cx="6" cy="6" rx="2.4" ry="5.5" stroke="#fff" stroke-width="0.7" fill="none"/></svg>
      www.qrt-beratung.de
    </p>
  </section>

  <section class="card card--licence" aria-label="Lizenzseite">
    <div class="licence">
      <p class="licence__label">LIZENSSCHLÜSSEL</p>
      <p class="licence__key">8416 9072 5831 6049</p>
    </div>
    <span class="rule rule--top"></span>
    <span class="rule rule--bottom"></span>

    <div class="brand">
      <span class="brand__mark"></span>
      <span class="brand__name">qrt quandt, reiter &amp; thal</span>
    </div>
  </section>

</body>
</html>
```